HALVERN BRIDGE LIMITED CALENDAR 2018

We need an innovative calendar design for our company for 2018. to give a brief description of our company:
"Halvern Bridge was founded in 2016 to provide a wide range of management consultancy and advisory services to small and medium-sized companies operating in consumer-driven sectors. With more than 300 years of cumulative investment and advisory experience among our sector-focused seasoned professionals, we advise management teams on an aggregate of $850m worth of investments operating in the healthcare, education, food and beverage and logistics sectors within the MENASEA region; the region of our expertise."
We want the design to include the following 12 countries for each month:
1. UAE 2. Saudi Arabia 3. Kuwait 4. Bahrain 5. Qatar 6. Oman 7. Jordan 8. Egypt 9. Singapore 10. Malaysia 11. Thailand 12. Indonesia
The description/design for each month must include each country's economic growth, Per Capita Income, GDP, etc. That is what we wish for the final design for each month to communicate as our company is in to a wide range of Investment management and Advisory Services
Target Market(s)
FINANCIAL SERVICES AND CONSULTING
Industry/Entity Type
Financial Service
Font styles to use
Colors
Designer to choose colors to be used in the design.
Look and feel

```html
<!DOCTYPE html>
<html lang="en">
<head>
<meta charset="utf-8">
<title>Halvern Bridge Calendar 2018 – February</title>
<link rel="stylesheet" href="https://fonts.googleapis.com/css2?family=Open+Sans:ital,wght@0,400;0,600;0,700;1,400;1,600;1,700&family=Berkshire+Swash&display=swap">
<style>
  :root {
    --gold: #c19a2e;
    --gold-dark: #a47f1c;
    --maroon: #8e1b2c;
    --ink: #1a1a1a;
    --grey-cell: #ececec;
    --grey-line: #b9b9b9;
    --navy-band: rgba(22, 30, 62, 0.94);
    --white: #ffffff;
  }
  * { box-sizing: border-box; margin: 0; padding: 0; }
  html, body { width: 1200px; height: 847px; overflow: hidden; background: #ffffff; }
  body { font-family: "Open Sans", Arial, sans-serif; color: var(--ink); }

  .calendar-page { position: relative; width: 1200px; height: 847px; overflow: hidden; background: var(--white); }

  .backdrop { position: absolute; inset: 0; }

  /* Month header */
  .year {
    position: absolute; left: 676px; top: 64px;
    font-weight: 700; font-size: 58px; color: var(--gold); letter-spacing: 1px;
  }
  .year-rule { position: absolute; left: 664px; top: 138px; width: 240px; height: 4px; background: var(--gold); }
  .month {
    position: absolute; right: 26px; top: 52px;
    font-family: "Berkshire Swash", cursive; font-size: 64px; color: var(--maroon); line-height: 1;
    white-space: nowrap;
  }

  /* Grid */
  .month-grid {
    position: absolute; left: 666px; top: 182px; width: 506px;
    border-collapse: collapse; table-layout: fixed;
  }
  .month-grid th {
    height: 20px; background: #d9d9d9; color: var(--maroon);
    font-size: 15px; font-weight: 700; text-align: left; padding-left: 6px;
  }
  .month-grid td {
    height: 53px; vertical-align: top; padding: 6px 0 0 6px;
    font-size: 17px; font-weight: 700; color: var(--ink);
    border-top: 2px solid var(--grey-line);
    border-left: 8px solid var(--white);
  }
  .month-grid td:first-child { border-left: 0; }
  .month-grid .weekend { background: var(--grey-cell); }

  /* Company block */
  .brand {
    position: absolute; left: 716px; top: 514px;
    display: flex; align-items: center; gap: 12px;
  }
  .brand-mark { width: 14px; height: 14px; background: var(--maroon); }
  .brand-name { font-size: 28px; font-weight: 700; color: var(--gold); letter-spacing: 4px; white-space: nowrap; }
  .about {
    position: absolute; left: 740px; top: 582px; width: 440px;
    font-size: 12.5px; line-height: 1.35; color: var(--ink);
  }
  .about strong { font-style: italic; }
  .motto {
    position: absolute; left: 760px; top: 636px;
    font-size: 16px; font-style: italic; color: var(--ink);
  }
  .web-bar {
    position: absolute; left: 882px; top: 666px; width: 318px; height: 32px;
    background: var(--gold-dark); border-radius: 16px 0 0 16px;
    color: var(--white); font-weight: 700; font-size: 17px;
    display: flex; align-items: center; padding-left: 26px;
  }

  /* Economic band */
  .economy-band { position: absolute; left: 0; top: 725px; width: 1200px; height: 122px; background: var(--navy-band); color: var(--white); }
  .country { position: absolute; left: 130px; top: 8px; display: flex; align-items: center; gap: 8px; }
  .country-name { font-size: 38px; font-weight: 700; color: var(--gold); }
  .country-caption { position: absolute; left: 133px; top: 78px; font-size: 15px; }
  .stats-year { position: absolute; left: 750px; top: 4px; font-size: 30px; font-weight: 700; }
  .stats-rule { position: absolute; left: 420px; top: 50px; width: 760px; height: 2px; background: var(--white); }
  .stat { position: absolute; top: 54px; }
  .stat-label { font-size: 15px; font-weight: 700; font-style: italic; }
  .stat-value { font-size: 22px; font-weight: 700; margin-top: 4px; }
  .stat-population { left: 431px; }
  .stat-gdp { left: 745px; }
  .stat-income { left: 975px; }
</style>
</head>
<body>
<main class="calendar-page">
  <svg class="backdrop" width="1200" height="847" viewBox="0 0 1200 847">
    <defs>
      <linearGradient id="duskSky" x1="0" y1="0" x2="0" y2="1">
        <stop offset="0" stop-color="#2a3b8f"/>
        <stop offset="0.35" stop-color="#5a4fb0"/>
        <stop offset="0.5" stop-color="#c77bb8"/>
        <stop offset="0.58" stop-color="#2c3f7e"/>
        <stop offset="1" stop-color="#15224d"/>
      </linearGradient>
    </defs>
    <polygon points="0,0 400,0 700,725 0,725" fill="url(#duskSky)" role="img" aria-label="Photograph of Kuwait's city towers and a traditional dhow on the water at dusk"/>
    <polygon points="385,0 520,0 760,725 705,725" fill="#c19a2e"/>
    <polygon points="520,0 545,0 770,725 760,725" fill="#d9d9d9"/>
  </svg>

  <div class="year">2018</div>
  <div class="year-rule"></div>
  <div class="month">February</div>

  <table class="month-grid">
    <thead>
      <tr><th>Sun</th><th>Mon</th><th>Tue</th><th>Wed</th><th>Thu</th><th>Fri</th><th>Sat</th></tr>
    </thead>
    <tbody>
      <tr><td></td><td></td><td></td><td></td><td>1</td><td>2</td><td class="weekend">3</td></tr>
      <tr><td>4</td><td>5</td><td>6</td><td>7</td><td>8</td><td>9</td><td class="weekend">10</td></tr>
      <tr><td>11</td><td>12</td><td>13</td><td>14</td><td>15</td><td>16</td><td class="weekend">17</td></tr>
      <tr><td>18</td><td>19</td><td>20</td><td>21</td><td>22</td><td>23</td><td class="weekend">24</td></tr>
      <tr><td>25</td><td>26</td><td>27</td><td>28</td><td></td><td></td><td class="weekend"></td></tr>
    </tbody>
  </table>

  <div class="brand">
    <span class="brand-mark"></span>
    <span class="brand-name">HALVERN BRIDGE</span>
  </div>
  <p class="about"><strong>Halvern Bridge</strong> was founded in 2016 to provide a wide range of management consultancy and advisory services to small and medium-sized companies operating in consumer-driven sectors.</p>
  <p class="motto">"Working with you towards building a better business..."</p>
  <div class="web-bar">www.halvern-bridge.com</div>

  <section class="economy-band">
    <div class="country">
      <svg width="30" height="42" viewBox="0 0 30 42" aria-hidden="true">
        <path d="M15 1C7.3 1 1 7.3 1 15c0 10.5 14 26 14 26s14-15.5 14-26C29 7.3 22.7 1 15 1z" fill="#c19a2e"/>
        <circle cx="15" cy="15" r="5.5" fill="#161e3e"/>
      </svg>
      <span class="country-name">Kuwait</span>
    </div>
    <div class="country-caption">Country's Economic Growth:</div>
    <div class="stats-year">2017</div>
    <div class="stats-rule"></div>
    <div class="stat stat-population"><div class="stat-label">Population</div><div class="stat-value">4.13 million</div></div>
    <div class="stat stat-gdp"><div class="stat-label">GDP</div><div class="stat-value">USD 124.9 billion</div></div>
    <div class="stat stat-income"><div class="stat-label">Per Capita Income</div><div class="stat-value">USD 28,756.2</div></div>
  </section>
</main>
</body>
</html>
```